Bright Harbor Design

We need a web design for our startup company based in Zurich, Switzerland called Bright Harbor. We offer professional flirt and dating advice, self development with seminars and practical coachings.

The final website aims for two capital goals. First, it will contain text, pictures and video based content presenting and advertising our services. Furthermore, we want to bind our costumers with a plattform offering them to share their expiriences related with our services.

The targeted group will be men from 25 to 40 years.
Updates

The design requires also a register-box to put in the clients Name and Email

I need (besides of the "email registration box") a "Video Gallery", "Blog" and "Agenda (with the next events to come)"

Target Market(s)

Guys around 25 to 40 years who want to improve their social lifestyle

Industry/Entity Type

Advertising

Requirements
Must have
• First and foremost, the design must transfer strong emotions and suggest an attractive social lifestyle.

The design should not be overloaded with content but should include pictures, videos and text.

The design should present a modern, urban lifestyle.
Nice to have
• There is a logo attached to the assignement. However, if you have a good idea for an improved or different logo, please do not hesitate to design your ideas.

```html
<!DOCTYPE html>
<html lang="en">
<head>
<meta charset="utf-8">
<title>Bright Harbor – Dating Advice &amp; Coaching</title>
<link rel="stylesheet" href="https://fonts.googleapis.com/css2?family=Questrial&family=Arimo:wght@400;700&family=Libre+Baskerville:wght@700&display=swap">
<style>
:root{
  --navy:#13284a;
  --navy-deep:#0e1f3b;
  --beige:#e9e6dc;
  --beige-light:#f3f1ea;
  --orange:#f7941d;
  --orange-red:#f26522;
  --red:#c1272d;
  --text:#1b2233;
  --muted:#6b6f78;
  --panel:#dedede;
  --white:#ffffff;
  --link-active:#f7941d;
}
*{box-sizing:border-box;margin:0;padding:0}
html,body{width:1140px;height:1200px;overflow:hidden}
body{background:var(--navy);font-family:"Questrial",sans-serif;color:var(--text);position:relative}
.abs{position:absolute}

/* header */
.site-header{left:0;top:0;width:1140px;height:120px;background:var(--beige)}
.brand{left:37px;top:34px;display:flex;align-items:center;gap:14px}
.brand-mark{width:44px;height:44px;border-radius:50%;background:var(--navy)}
.brand-name{font-size:34px;color:var(--navy);letter-spacing:.5px}
.login{left:523px;top:14px}
.login-label{font-size:16px;color:#555;margin-bottom:8px}
.login-field{width:175px;height:22px;border:2px solid #cfcbbd;background:linear-gradient(#efede6,#fbfaf6);margin-bottom:13px}
.login-go{left:708px;top:46px;width:44px;height:44px;border-radius:50%;background:radial-gradient(circle at 40% 35%,#ff5a4a,#c1151b);color:#fff;font-family:"Arimo",sans-serif;font-weight:700;font-size:13px;display:flex;align-items:center;justify-content:center}
.header-arrow{left:725px;top:0}
.main-nav{left:780px;top:0;height:120px;display:flex}
.nav-item{display:flex;flex-direction:column;align-items:center;justify-content:center;gap:6px;font-size:19px;color:#333;height:120px}
.nav-item.home{width:88px}
.nav-item.services{width:135px;background:linear-gradient(90deg,#dcd8cb,var(--beige-light) 20%,var(--beige-light) 80%,#dcd8cb)}
.nav-item.contact{width:110px}

/* hero */
.hero{left:33px;top:143px;width:1073px;height:430px;background:var(--beige);}
.hero-tabs{left:38px;top:148px;display:flex;height:54px}
.tab{display:flex;align-items:center;color:#fff;font-size:18px;padding:0 18px 0 12px;height:54px;clip-path:polygon(0 0,calc(100% - 18px) 0,100% 50%,calc(100% - 18px) 100%,0 100%)}
.tab.advice{background:var(--orange);width:128px}
.tab.develop{background:var(--orange-red);width:170px;margin-left:-4px;padding-left:24px}
.tab.coach{background:var(--red);width:204px;margin-left:-4px;padding-left:24px}
.hero-strip{left:555px;top:143px;width:551px;height:55px;background:var(--navy)}
.free-claim{left:566px;top:143px;font-family:"Arimo",sans-serif;font-weight:700;font-size:30px;color:var(--orange);line-height:36px}
.wallet-note{left:740px;top:151px;font-size:21px;color:#d7dbe3}
.join-now{left:969px;top:136px;width:128px;height:45px;border:1px solid #8aa0c8;background:linear-gradient(#22395f,#0c1a33);color:#d7e3ff;font-size:20px;display:flex;align-items:center;justify-content:center}
.hero-media{left:38px;top:202px;width:1063px;height:368px;background:linear-gradient(100deg,#8a5a3a 0%,#c79a5a 35%,#5a4a40 55%,#9aa2ab 75%,#d9dde2 100%)}
.play{left:843px;top:306px}
.hero-caption{left:38px;top:518px;width:405px;height:52px;background:linear-gradient(90deg,rgba(15,30,55,.9),rgba(15,30,55,.6));clip-path:polygon(0 0,92% 0,100% 100%,0 100%);color:#fff;font-size:21px;padding:12px 0 0 20px}

/* content panel */
.content{left:22px;top:573px;width:1095px;height:550px;background:var(--white)}
.signup-card{left:44px;top:601px;width:304px;height:211px;border:1px solid #ccc;border-radius:6px;background:#fff;box-shadow:0 1px 4px rgba(0,0,0,.25);padding:6px}
.signup-inner{position:relative;width:100%;height:100%;background:linear-gradient(135deg,#1c4f9c,#0f2d6b);overflow:hidden}
.signup-roses{right:0;top:0;width:110px;height:100%;background:linear-gradient(160deg,#b3202a,#6d1016 60%,#2e6a3a)}
.signup-free{left:-32px;top:78px;transform:rotate(-90deg);font-family:"Libre Baskerville",serif;font-size:38px;color:#fff;letter-spacing:2px}
.signup-title{left:78px;top:16px;font-family:"Libre Baskerville",serif;font-size:27px;line-height:32px;color:#fff}
.signup-btn{left:77px;top:139px;width:133px;height:36px;border-radius:6px;background:linear-gradient(#ffb347,#f07a10);font-family:"Arimo",sans-serif;font-weight:700;font-size:16px;color:#222;display:flex;align-items:center;justify-content:center;gap:6px}
.signup-btn i{width:16px;height:16px;border-radius:50%;background:var(--red);display:inline-block}

.welcome{left:381px;top:603px;width:378px}
.welcome h1{font-weight:400;font-size:22px;color:var(--navy);letter-spacing:.5px;padding-bottom:10px;border-bottom:1px solid #ddd;margin-bottom:10px}
.welcome p{font-family:"Arimo",sans-serif;font-size:13.5px;line-height:21px;text-align:justify;color:#111;margin-bottom:10px}
.welcome .more{text-align:right;font-size:14.5px;font-family:"Questrial",sans-serif;margin-top:-6px}

.side-box{width:304px;background:var(--panel);border-radius:6px;overflow:hidden}
.side-box h2{font-weight:400;font-size:21px;color:#fff;background:linear-gradient(#223d66,var(--navy));height:44px;padding:8px 0 0 20px;letter-spacing:.5px}
.quick-search{left:791px;top:602px;height:223px}
.select,.input{position:absolute;height:28px;border:1px solid #bbb;border-radius:3px;background:linear-gradient(#c9c9c9,#e4e4e4);font-size:14px;color:#777;padding:5px 8px}
.select::after{content:"";position:absolute;right:0;top:0;width:23px;height:26px;background:var(--navy-deep)}
.select b{position:absolute;right:6px;top:10px;width:0;height:0;border-left:5px solid transparent;border-right:5px solid transparent;border-top:6px solid #fff;z-index:1}
.to{position:absolute;left:145px;top:100px;font-size:14px}
.search-btn{position:absolute;left:98px;top:178px;width:108px;height:30px;border-radius:3px;background:linear-gradient(#ffb347,#f07a10);font-size:14.5px;display:flex;align-items:center;justify-content:center;color:#222}

.members-title{left:44px;top:860px;width:712px;text-align:center;font-size:21px;color:var(--navy);letter-spacing:.5px}
.members-arc{left:60px;top:876px;width:680px;height:26px;background:radial-gradient(ellipse at 50% 100%,#e6e6e6,#fff 70%)}
.carousel{left:44px;top:900px;width:712px;height:187px;border:1px solid #ccc;border-radius:6px;background:#eee}
.car-btn{position:absolute;top:3px;width:40px;height:179px;background:#a9a9a9;display:flex;align-items:center;justify-content:center}
.car-btn.prev{left:3px}.car-btn.next{right:3px}
.member{position:absolute;top:16px;width:138px;height:154px}
.m1{left:57px;background:linear-gradient(#3a4350,#1e242c)}
.m2{left:210px;background:linear-gradient(#8b5a35,#3d2a20)}
.m3{left:363px;background:linear-gradient(#c9cdd1,#6d655c)}
.m4{left:516px;background:linear-gradient(#d6d8da,#3a3a3a)}

.success{left:791px;top:865px;height:222px}
.story{position:relative;padding:12px 16px;font-family:"Arimo",sans-serif;font-size:13.5px;line-height:20px;color:#111}
.story-photo{float:left;width:80px;height:72px;border:3px solid #fff;box-shadow:0 1px 3px rgba(0,0,0,.35);background:linear-gradient(#7a6a5e,#3a332e);margin:2px 14px 4px 0}
.story-name{font-family:"Questrial",sans-serif;font-size:19px;color:var(--navy);line-height:22px;margin-bottom:2px}
.q{font-family:"Libre Baskerville",serif;color:#777;font-size:18px}
.story-more{clear:both;text-align:right;font-style:italic;font-size:14px;padding-top:6px;padding-right:10px}

/* footer */
.footer-nav{left:0;top:1137px;width:1140px;text-align:center;font-size:14.5px;color:#d8dde6}
.footer-nav span{color:#5e6f8d;margin:0 9px}
.footer-nav .active{color:var(--link-active)}
.copyright{left:0;top:1166px;width:1140px;text-align:center;font-size:13px;color:#8391ab}
</style>
</head>
<body>

<header class="abs site-header">
  <div class="abs brand"><span class="brand-mark"></span><span class="brand-name">Bright Harbor</span></div>
  <div class="abs login">
    <div class="login-label">Member Login</div>
    <div class="login-field"></div>
    <div class="login-field"></div>
  </div>
  <div class="abs login-go">GO</div>
  <svg class="abs header-arrow" width="60" height="120" viewBox="0 0 60 120"><polyline points="1,0 45,60 1,120" fill="none" stroke="#fff" stroke-width="2"/></svg>
  <nav class="abs main-nav">
    <div class="nav-item home">
      <svg width="22" height="20" viewBox="0 0 22 20"><path d="M11 1 L1 10 H4 V19 H9 V13 H13 V19 H18 V10 H21 Z" fill="#111"/></svg>
      Home</div>
    <div class="nav-item services">
      <svg width="24" height="24" viewBox="0 0 24 24"><circle cx="12" cy="12" r="8" fill="none" stroke="#111" stroke-width="4" stroke-dasharray="3 2.3"/><circle cx="12" cy="12" r="6" fill="#111"/><circle cx="12" cy="12" r="2.5" fill="#f3f1ea"/></svg>
      our services</div>
    <div class="nav-item contact">
      <svg width="26" height="18" viewBox="0 0 26 18"><rect x="0" y="0" width="26" height="18" fill="#111"/><polyline points="1,1 13,10 25,1" fill="none" stroke="#e9e6dc" stroke-width="2"/></svg>
      Contact</div>
  </nav>
</header>

<section class="abs hero"></section>
<div class="abs hero-strip"></div>
<div class="abs free-claim">100% free!</div>
<div class="abs wallet-note">No wallet necessary</div>
<div class="abs join-now">JOIN NOW</div>
<div class="abs hero-media" role="img" aria-label="Video still: a man chatting with a woman in a market shop and smiling while talking to a woman on a city street"></div>
<div class="abs hero-tabs">
  <div class="tab advice">Dating Advice</div>
  <div class="tab develop">Self Development</div>
  <div class="tab coach">Practical Coachings</div>
</div>
<svg class="abs play" width="106" height="106" viewBox="0 0 106 106" aria-label="Play video">
  <circle cx="53" cy="53" r="48" fill="none" stroke="#c8170f" stroke-width="6" stroke-dasharray="120 14"/>
  <circle cx="53" cy="53" r="37" fill="#c8170f"/>
  <polygon points="43,35 43,71 72,53" fill="#fff"/>
</svg>
<div class="abs hero-caption">Where Single Friends Create Pairs</div>

<main class="abs content"></main>

<div class="abs signup-card">
  <div class="signup-inner">
    <div class="abs signup-roses" role="img" aria-label="Bouquet of red roses"></div>
    <div class="abs signup-free">FREE</div>
    <div class="abs signup-title">100%<br>PROFILE<br>SIGN UP</div>
    <div class="abs signup-btn"><i></i>Join Now!</div>
  </div>
</div>

<article class="abs welcome">
  <h1>Welcome to our datting site!</h1>
  <p>Lorem ipsum dolor sit amet, consectetur adipiscing elit. Sed euismod facilisis ligula, at fermentum nisl rutrum a. Nunc diam odio, hendrerit eget euismod quis, tempor eu sem. Nulla eget odio vitae tortor gravida accumsan sit amet vel arcu.</p>
  <p>odio vitae tortor gravida accumsan sit amet vel arcu.rutrum a. Nunc diam odio, hendrerit</p>
  <div class="more">Read more...</div>
</article>

<aside class="abs side-box quick-search">
  <h2>Quick Search</h2>
  <div style="position:relative">
    <div class="select" style="left:10px;top:12px;width:121px"><b></b>I am</div>
    <div class="select" style="left:146px;top:12px;width:121px"><b></b>Seeking a</div>
    <div class="select" style="left:10px;top:51px;width:121px"><b></b>18</div>
    <span class="to" style="top:58px;left:134px">to</span>
    <div class="select" style="left:156px;top:51px;width:111px"><b></b>35</div>
    <div class="select" style="left:10px;top:91px;width:121px"><b></b>Country:</div>
    <div class="input" style="left:146px;top:91px;width:121px;background:linear-gradient(#d0d0d0,#e6e6e6)">Zip code</div>
    <div class="search-btn" style="top:134px">Search Now</div>
  </div>
</aside>

<div class="abs members-arc"></div>
<h2 class="abs members-title" style="font-weight:400">New Members</h2>
<div class="abs carousel">
  <div class="car-btn prev"><svg width="16" height="40" viewBox="0 0 16 40"><polyline points="13,2 3,20 13,38" fill="none" stroke="#13284a" stroke-width="4"/></svg></div>
  <div class="member m1" role="img" aria-label="New member profile photo"></div>
  <div class="member m2" role="img" aria-label="New member profile photo"></div>
  <div class="member m3" role="img" aria-label="New member profile photo"></div>
  <div class="member m4" role="img" aria-label="New member profile photo"></div>
  <div class="car-btn next"><svg width="16" height="40" viewBox="0 0 16 40"><polyline points="3,2 13,20 3,38" fill="none" stroke="#13284a" stroke-width="4"/></svg></div>
</div>

<aside class="abs side-box success">
  <h2>Success stories</h2>
  <div class="story">
    <div class="story-photo" role="img" aria-label="Customer portrait"></div>
    <div class="story-name">customer Name</div>
    <span class="q">“</span> Lorem ipsum dolor sit amet, consectetur adipiscing elit. Lorem ipsum Lorem ipsum dolor sit amet, consectetur adipiscing elit. Sed euismod <span class="q">”</span>
    <div class="story-more">Read more Stories</div>
  </div>
</aside>

<nav class="abs footer-nav">
  <span class="active" style="margin:0">Home</span><span>/</span>About Us<span>/</span>Success Stories<span>/</span>our services<span>/</span>FAQ<span>/</span>News<span>/</span>Contact Us<span>/</span>Terms of Use<span>/</span>Privacy Policy
</nav>
<div class="abs copyright">© 2013 Bright Harbor. All Rights Reserved.</div>

</body>
</html>
```